Brelton Services - Fast, Efficient and Gas Mainteance for Domestic, Commercial and Industrial clients

We are in the process of purchasing a new business and would like to get a new logo and business card.
Business is a gas maintenance business that also does new gas installations.
Has been established since 1988.
Services include:
Install all types of gas appliances & equipment inc. hot water units
Maintain / repair / replace all types of gas appliances & equipment

Target Market(s)

Domestic, Commercial and Industrial clients

Industry/Entity Type

Business

Contact Information for Business Card

admin@breltonservices.example.au
07 5382 4690
Brelton Services PTY LTD

Logo Text

Gas Fitting & Plumbing Maintenance Specialists

Font styles to use
Sans Serif

Requirements
Must have
• Logo
• Business name, contact number, email address, web address
• Domestic | Commercial | Industrial Est Since 1988
Nice to have
• Possibly a black card with a flame logo to one side
Should not have
• Spelling errors

```html
<!DOCTYPE html>
<html lang="en">
<head>
<meta charset="utf-8">
<title>Brelton Services PTY LTD – Business Card</title>
<link rel="stylesheet" href="https://fonts.googleapis.com/css2?family=Source+Sans+3:wght@400&display=swap">
<style>
  :root {
    --page-bg: #ecebea;
    --card-bg: #fbfbfb;
    --card-edge: #e2e0de;
    --brand-yellow: #f2c417;
    --text-red: #e3202a;
    --icon-orange: #f07a22;
    --rule-red: #ef8a8a;
  }
  * { margin: 0; padding: 0; box-sizing: border-box; }
  html, body {
    width: 1200px;
    height: 900px;
    overflow: hidden;
    background: var(--page-bg);
    font-family: "Source Sans 3", "Myriad Pro", Arial, sans-serif;
  }
  .business-card {
    position: absolute;
    left: 150px;
    top: 173px;
    width: 900px;
    height: 554px;
    background: var(--card-bg);
    border: 1px solid var(--card-edge);
    border-radius: 22px;
    box-shadow: 0 10px 30px rgba(0,0,0,0.08);
  }
  .brand-name {
    position: absolute;
    left: 72px;
    top: 178px;
    color: var(--brand-yellow);
    font-weight: 400;
    line-height: 1;
  }
  .brand-name .brand-word {
    display: block;
    font-size: 80px;
    letter-spacing: 1px;
  }
  .brand-name .brand-suffix {
    display: block;
    margin-top: 6px;
    margin-left: 12px;
    font-size: 21px;
    letter-spacing: 3.4px;
  }
  .contact-list {
    position: absolute;
    left: 485px;
    top: 150px;
    list-style: none;
  }
  .contact-list li {
    display: flex;
    align-items: center;
    height: 32.5px;
    font-size: 23px;
    color: var(--text-red);
  }
  .contact-list svg {
    width: 16px;
    height: 16px;
    margin-right: 12px;
    flex: none;
  }
  .postal-address {
    position: absolute;
    left: 485px;
    top: 298px;
    font-style: normal;
    font-size: 23px;
    line-height: 32px;
    color: var(--text-red);
  }
  .service-strip {
    position: absolute;
    left: 0;
    top: 446px;
    width: 100%;
    display: flex;
    align-items: center;
    gap: 20px;
  }
  .service-strip .rule {
    flex: 1;
    height: 1.5px;
    background: var(--rule-red);
  }
  .service-strip .rule.left { flex: 0 0 146px; }
  .service-strip .rule.right { flex: 0 0 146px; }
  .service-strip p {
    font-size: 23px;
    color: var(--text-red);
    white-space: nowrap;
  }
</style>
</head>
<body>
  <section class="business-card">
    <div class="brand-name">
      <span class="brand-word">Brelton</span>
      <span class="brand-suffix">SERVICES PTY LTD</span>
    </div>

    <ul class="contact-list">
      <li>
        <svg viewBox="0 0 16 16" aria-hidden="true"><path fill="var(--icon-orange)" d="M3.2 1.5l2.3-.4 1.3 3.2-1.6 1.2c.8 1.8 2.2 3.2 4 4l1.2-1.6 3.2 1.3-.4 2.3c-.2.8-.9 1.3-1.7 1.2C6.5 12.3 3.7 9.5 2 4.3c-.2-.8.3-1.6 1.2-1.8z"/></svg>
        07 5382 4690
      </li>
      <li>
        <svg viewBox="0 0 16 16" aria-hidden="true"><rect x="1" y="3" width="14" height="10" rx="1" fill="var(--icon-orange)"/><path d="M1.5 3.8L8 9l6.5-5.2" fill="none" stroke="#fff" stroke-width="1.3"/></svg>
        admin@breltonservices.example.au
      </li>
      <li>
        <svg viewBox="0 0 16 16" aria-hidden="true"><circle cx="8" cy="8" r="6.5" fill="none" stroke="var(--icon-orange)" stroke-width="1.4"/><ellipse cx="8" cy="8" rx="2.8" ry="6.5" fill="none" stroke="var(--icon-orange)" stroke-width="1.2"/><path d="M1.5 8h13M2.6 4.8h10.8M2.6 11.2h10.8" stroke="var(--icon-orange)" stroke-width="1.1"/></svg>
        www.breltonservices.example.au
      </li>
    </ul>

    <address class="postal-address">
      12345, Address Goes Here<br>
      Country Name, 123456.
    </address>

    <div class="service-strip">
      <span class="rule left"></span>
      <p>Domestic | Commercial | Industrial Est Since 1988</p>
      <span class="rule right"></span>
    </div>
  </section>
</body>
</html>
```